Business Card Design

I need a design/ business card for a new company that caters for Event Hire (decorations and linen only) I am dabbling in rustic/ vintage designs for weddings and would like an elegant look to the cards. Something that will catch peoples eyes amongst the rest of the competitions cards and stand out to all fields, corporate/ weddings and general functions.

I am unsure of colours or pictures i would like so i am open to anything but possibly stick away from photos as i they are not more work of art on the card?
Updates

Target Market(s)

weddings and corporate events

Industry/Entity Type

Business

Contact Information for Business Card

Marlowe Weddings & Event Hire

Servicing the Gladstone Region for Weddings, Corporate & Private Functions

marloweweddings@postvale.net
Phone: 0427 814 253

Requirements
Must have
• The writing "Marlowe Weddings & Event Hire" please
Nice to have
• Something that really stands out as a must have at your event
Should not have
• Pictures that are not of my work

```html
<!DOCTYPE html>
<html lang="en">
<head>
<meta charset="utf-8">
<title>Marlowe Weddings &amp; Event Hire – Business Card</title>
<link rel="stylesheet" href="https://fonts.googleapis.com/css2?family=Open+Sans:wght@400;600;700&display=swap">
<style>
  :root {
    --page: #e8e3da;
    --card: #fdf2dc;
    --mauve: #7a5f65;
    --mauve-deep: #6a5056;
    --accent-red: #e3262c;
    --cream-text: #fdf2dc;
  }
  * { margin: 0; padding: 0; box-sizing: border-box; }
  html, body {
    width: 1200px; height: 870px; overflow: hidden;
    background: var(--page);
    font-family: "Open Sans", Arial, sans-serif;
  }
  .business-card {
    position: absolute; left: 100px; top: 170px;
    width: 1000px; height: 530px;
    background: var(--card);
    border-radius: 30px;
    overflow: hidden;
    box-shadow: 0 6px 18px rgba(60, 45, 40, 0.18);
  }
  .ornament {
    position: absolute; top: 48px;
    width: 175px; height: 115px;
    border-radius: 50%;
  }
  .ornament--left {
    left: 50px;
    background: radial-gradient(ellipse at 60% 50%, rgba(227, 38, 44, 0.55), rgba(227, 38, 44, 0.08) 70%, transparent 72%);
  }
  .ornament--right {
    right: 50px;
    background: radial-gradient(ellipse at 40% 50%, rgba(227, 38, 44, 0.55), rgba(227, 38, 44, 0.08) 70%, transparent 72%);
  }
  .brand-name {
    position: absolute; left: 0; right: 0; top: 38px;
    text-align: center;
    font-weight: 600; font-size: 96px; letter-spacing: 4px;
    color: var(--mauve); line-height: 1;
  }
  .brand-tagline {
    position: absolute; left: 232px; right: 225px; top: 150px;
    text-align: right;
    font-weight: 400; font-size: 33px; letter-spacing: 3px;
    color: var(--mauve); line-height: 1;
  }
  .contact-list {
    position: absolute; left: 232px; top: 225px;
    list-style: none;
  }
  .contact-item {
    display: flex; align-items: center; gap: 42px;
    height: 40px;
    font-weight: 700; font-size: 21px; color: var(--mauve);
  }
  .contact-icon { width: 22px; height: 22px; flex: none; }
  .service-band {
    position: absolute; left: 0; right: 0; top: 338px; height: 78px;
    background: var(--mauve);
    color: var(--cream-text);
    text-align: center;
    font-size: 23px; letter-spacing: 2.5px; line-height: 31px;
    padding-top: 6px;
  }
  .grain-pattern {
    position: absolute; left: 0; right: 0; top: 416px; bottom: 0;
    background: linear-gradient(180deg, #cdbcb6 0%, #a68e90 55%, var(--mauve-deep) 100%);
  }
</style>
</head>
<body>
  <main class="business-card">
    <div class="ornament ornament--left" role="img" aria-label="Red calligraphic flourish ornament"></div>
    <div class="ornament ornament--right" role="img" aria-label="Red calligraphic flourish ornament"></div>

    <h1 class="brand-name">MARLOWE</h1>
    <p class="brand-tagline">WEDDING &amp; EVENT HIRE</p>

    <ul class="contact-list">
      <li class="contact-item">
        <svg class="contact-icon" viewBox="0 0 22 22" aria-hidden="true">
          <rect x="2" y="5" width="18" height="12" fill="none" stroke="#7a5f65" stroke-width="1.6"/>
          <path d="M2 5 L11 12 L20 5 M2 17 L9 10.5 M20 17 L13 10.5" fill="none" stroke="#7a5f65" stroke-width="1.4"/>
        </svg>
        <span>marloweweddings@postvale.net</span>
      </li>
      <li class="contact-item">
        <svg class="contact-icon" viewBox="0 0 22 22" aria-hidden="true">
          <rect x="2" y="2" width="18" height="18" rx="3" fill="#7a5f65"/>
          <path d="M13 6 C9 6 8 9 8 11 C8 13 9 16 13 16 L13 14 C11 14 10.5 12.5 10.5 11 C10.5 9.5 11 8 13 8 Z" fill="#fdf2dc"/>
        </svg>
        <span>0427 814 253</span>
      </li>
    </ul>

    <section class="service-band">
      <p>SERVICING THE GLADSTONE REGION FOR:</p>
      <p>WEDDINGS &nbsp;I&nbsp; CORPORATE FUNCTION &nbsp;I PRIVATE FUNCTIONS</p>
    </section>

    <div class="grain-pattern" role="img" aria-label="Decorative wood-grain line pattern in mauve"></div>
  </main>
</body>
</html>
```